Tech Company Letterhead/Business Cards/Envelopes

We would like a new stationary design for a technology company that develops full turnkey solutions for governments related to Data, Identity Tracking, Fingerprinting, Passport Control, and Border Protection Systems.

We would like the stationary designs to include:

Letter Head
Business Cards
Envelopes

Target Market(s)

Corporate

Industry/Entity Type

Business

Contact Information for Business Card

Details to be shared with the winner.

Font styles to use
Serif
Sans Serif

Colors
e4daeb
85abd2
3176b5
0355a3
0692cd

```html
<!DOCTYPE html>
<html lang="en">
<head>
<meta charset="utf-8">
<title>Norvak Stationery Set</title>
<link href="https://fonts.googleapis.com/css2?family=Arimo:wght@400;700&display=swap" rel="stylesheet">
<style>
  :root {
    --stage: #939395;
    --paper: #ffffff;
    --brand-blue: #1a74bb;
    --ink: #1c1c1c;
    --ink-soft: #555555;
    --rule-grey: #dcdcdc;
  }
  * { margin: 0; padding: 0; box-sizing: border-box; }
  html, body { width: 1189px; height: 1200px; overflow: hidden; }
  body {
    background: var(--stage);
    position: relative;
    font-family: "Arimo", Arial, sans-serif;
    color: var(--ink);
  }
  .sheet { position: absolute; background: var(--paper); }
  .wordmark {
    position: absolute;
    font-family: "Arimo", Arial, sans-serif;
    font-weight: 700;
    color: var(--brand-blue);
    letter-spacing: 0.06em;
    line-height: 1;
  }

  /* Letterhead */
  .letterhead { left: 50px; top: 110px; width: 508px; height: 657px; }
  .letterhead .wordmark { left: 42px; top: 54px; font-size: 40px; }
  .recipient { position: absolute; left: 40px; top: 150px; font-size: 9px; line-height: 1.25; }
  .recipient strong { display: block; font-size: 10px; font-weight: 400; margin-bottom: 3px; }
  .letter-body { position: absolute; left: 40px; top: 229px; width: 425px; font-size: 9.3px; line-height: 15px; }
  .letter-body p + p { margin-top: 15px; }
  .sign-off { position: absolute; left: 40px; top: 461px; font-size: 9.3px; }
  .signature-area { position: absolute; left: 40px; top: 480px; width: 118px; height: 34px; background: linear-gradient(90deg, #e9e9e9, #f6f6f6); }
  .signer { position: absolute; left: 40px; top: 523px; font-size: 9.5px; line-height: 1.3; }
  .signer strong { display: block; font-weight: 700; }
  .letter-footer { position: absolute; left: 43px; top: 598px; width: 421px; border-top: 2px solid var(--brand-blue); display: flex; padding-top: 8px; font-size: 8px; color: var(--ink-soft); line-height: 1.3; }
  .footer-col { display: flex; flex-direction: column; padding: 0 0 0 8px; }
  .footer-col + .footer-col { border-left: 1.5px solid var(--ink-soft); margin-left: 30px; padding-left: 26px; }
  .footer-col span { display: flex; align-items: center; gap: 4px; }
  .icon { width: 7px; height: 7px; flex: none; }

  /* Folder */
  .folder { left: 629px; top: 111px; width: 506px; height: 654px; }
  .folder-spine { position: absolute; left: 18px; top: 0; width: 4px; height: 100%; background: var(--rule-grey); }
  .folder .wordmark { left: 0; right: 0; text-align: center; top: 153px; font-size: 46px; }
  .folder-url { position: absolute; left: 0; right: 0; top: 609px; text-align: center; font-size: 8px; color: var(--ink-soft); }

  /* Envelopes */
  .envelope-front { left: 47px; top: 850px; width: 401px; height: 201px; }
  .envelope-front .wordmark { left: 23px; top: 26px; font-size: 26px; }
  .envelope-address { position: absolute; left: 23px; top: 59px; font-size: 6px; color: var(--ink-soft); }
  .envelope-back { left: 479px; top: 850px; width: 401px; height: 201px; overflow: hidden; }
  .envelope-flap { position: absolute; left: 0; top: 0; width: 401px; height: 60px; }
  .envelope-back .wordmark { left: 0; right: 0; text-align: center; top: 20px; font-size: 19px; }

  /* Business cards */
  .card { border-radius: 6px; width: 215px; }
  .card-front { left: 921px; top: 805px; height: 122px; }
  .card-front .wordmark { left: 0; right: 0; text-align: center; top: 48px; font-size: 24px; }
  .card-back { left: 921px; top: 953px; height: 123px; }
  .card-back .wordmark { left: 13px; top: 55px; font-size: 18px; }
  .card-divider { position: absolute; left: 111px; top: 32px; width: 1px; height: 60px; background: var(--brand-blue); }
  .card-details { position: absolute; left: 120px; top: 32px; font-size: 5.6px; line-height: 1.35; color: var(--ink-soft); }
  .card-details .card-name { font-size: 7px; font-weight: 700; color: var(--ink); }
  .card-details .card-role { color: var(--brand-blue); margin-bottom: 6px; }
  .card-details .card-address { margin-bottom: 3px; }
  .card-details span.line { display: flex; align-items: center; gap: 3px; }
  .card-details .icon { width: 5px; height: 5px; }
</style>
</head>
<body>

<section class="sheet letterhead">
  <div class="wordmark">NORVAK</div>
  <div class="recipient">
    <strong>ALAN REED</strong>
    Street Name, City Name.<br>
    Zip Code 0000
  </div>
  <div class="letter-body">
    <p>Lorem Ipsum is simply dummy text of the printing and typesetting industry. Lorem Ipsum has been the industry's standard dummy text ever since the 1500s, when an unknown printer took a galley of type and scrambled it to make a type specimen book. It has survived not only five centuries, but also the leap into electronic typesetting, remaining essentially unchanged. It was popularised in the 1960s with the release of Letraset sheets containing Lorem Ipsum passages, and more recently with desktop publishing software like Aldus PageMaker including versions of Lorem Ipsum.</p>
    <p>It is a long established fact that a reader will be distracted by the readable content of a page when looking at its layout. The point of using Lorem Ipsum is that it has a more-or-less normal distribution of letters, as opposed to using 'Content here, content here', making it look like readable English. Many desktop publishing packages and web page editors now use Lorem Ipsum as their default model text, and a search for 'lorem ipsum' will uncover many web sites still in their infancy. Various versions have evolved over the years, sometimes by accident, sometimes on purpose (injected humour and the like).</p>
  </div>
  <div class="sign-off">Regards,</div>
  <div class="signature-area" role="img" aria-label="Handwritten signature"></div>
  <div class="signer"><strong>Mara Quinn</strong>General Manager</div>
  <div class="letter-footer">
    <div class="footer-col">
      <span><svg class="icon" viewBox="0 0 10 10"><rect width="10" height="10" rx="1.5" fill="#1a74bb"/><path d="M3 2.5 4.3 4 3.8 4.8C4.4 5.8 5 6.3 5.6 6.6L6.4 6 7.6 7.2 7 8C4.8 7.6 2.7 5.3 2.3 3.2Z" fill="#fff"/></svg>555 018 2046</span>
      <span><svg class="icon" viewBox="0 0 10 10"><rect width="10" height="10" rx="1.5" fill="#1a74bb"/><rect x="2.5" y="3.5" width="5" height="3.5" fill="#fff"/></svg>555 018 2047</span>
    </div>
    <div class="footer-col">
      <span><svg class="icon" viewBox="0 0 10 10"><rect x="1" y="1" width="8" height="8" fill="none" stroke="#1a74bb" stroke-width="1.6"/></svg>hello@norvak-systems.com</span>
      <span><svg class="icon" viewBox="0 0 10 10"><circle cx="5" cy="5" r="4.5" fill="#1a74bb"/><path d="M1 5H9M5 1V9" stroke="#fff" stroke-width="0.8"/></svg>www.norvak-systems.com</span>
    </div>
    <div class="footer-col">
      <span>0000 Harbor Lane, 2nd Ste.</span>
      <span>Lakeview, State 1234</span>
    </div>
  </div>
</section>

<section class="sheet folder">
  <div class="folder-spine"></div>
  <div class="wordmark">NORVAK</div>
  <div class="folder-url">www.norvak-systems.com</div>
</section>

<section class="sheet envelope-front">
  <div class="wordmark">NORVAK</div>
  <div class="envelope-address">0000 Harbor Lane, 2nd Ste, Lakeview, State 1234</div>
</section>

<section class="sheet envelope-back">
  <svg class="envelope-flap" viewBox="0 0 401 60" aria-hidden="true">
    <path d="M0 0H401L392 52Q391 57 386 57H15Q10 57 9 52Z" fill="#ffffff" stroke="#cfcfcf" stroke-width="1.5"/>
  </svg>
  <div class="wordmark">NORVAK</div>
</section>

<section class="sheet card card-front">
  <div class="wordmark">NORVAK</div>
</section>

<section class="sheet card card-back">
  <div class="wordmark">NORVAK</div>
  <div class="card-divider"></div>
  <div class="card-details">
    <div class="card-name">ALAN REED</div>
    <div class="card-role">Manager</div>
    <div class="card-address">0000 Harbor Lane, 2nd Ste<br>Lakeview, State 1234</div>
    <span class="line"><svg class="icon" viewBox="0 0 10 10"><rect width="10" height="10" rx="1.5" fill="#1a74bb"/></svg>555 018 2046</span>
    <span class="line"><svg class="icon" viewBox="0 0 10 10"><rect x="1" y="1" width="8" height="8" fill="none" stroke="#1a74bb" stroke-width="1.6"/></svg>hello@norvak-systems.com</span>
    <span class="line"><svg class="icon" viewBox="0 0 10 10"><circle cx="5" cy="5" r="4.5" fill="#1a74bb"/></svg>www.norvak-systems.com</span>
  </div>
</section>

</body>
</html>
```